I need a logo design and a business card design for a new strategy consultancy that I set up called Tessaron LLC. We help clients make strategically important decisions, cutting through the cloud of noise. The design should imply clarity, simplicity and wisdom.

```html
<!DOCTYPE html>
<html lang="en">
<head>
<meta charset="utf-8">
<title>Tessaron LLC – Business Card</title>
<link href="https://fonts.googleapis.com/css2?family=Open+Sans:wght@400;600;700&display=swap" rel="stylesheet">
<style>
  :root {
    --teal: #00889a;
    --ink: #3a3a3a;
    --rule: #b8b8b8;
    --paper: #ffffff;
    --stage: #2f3133;
  }
  * { margin: 0; padding: 0; box-sizing: border-box; }
  html, body { width: 1200px; height: 896px; overflow: hidden; }
  body {
    background: var(--stage);
    font-family: "Open Sans", Arial, sans-serif;
    position: relative;
  }
  .card {
    position: absolute;
    left: 250px;
    width: 700px;
    height: 400px;
    overflow: hidden;
  }
  .card--front { top: 36px; background: var(--paper); border-bottom: 16px solid var(--teal); }
  .card--back { top: 460px; background: var(--teal); }

  .holder { position: absolute; left: 56px; top: 58px; }
  .holder__name {
    color: var(--teal); font-weight: 700; font-size: 30px;
    letter-spacing: 1px; text-transform: uppercase; line-height: 1.1;
  }
  .holder__title { color: var(--ink); font-size: 19px; margin-top: 2px; }

  .contact { position: absolute; left: 56px; top: 146px; list-style: none; }
  .contact__item {
    display: flex; align-items: center; gap: 10px;
    color: var(--ink); font-size: 19px; line-height: 30px;
  }
  .contact__icon { width: 16px; height: 16px; fill: var(--ink); flex: none; }

  .divider {
    position: absolute; left: 56px; right: 40px; top: 260px;
    height: 1px; background: var(--rule);
  }

  .brand {
    position: absolute; right: 56px; top: 178px;
    display: flex; align-items: center; gap: 12px;
  }
  .brand__mark { width: 22px; height: 22px; background: var(--teal); }
  .brand__name {
    font-weight: 600; font-size: 34px; letter-spacing: 3px;
    color: var(--ink); text-transform: uppercase;
  }

  .address {
    position: absolute; right: 56px; top: 282px;
    text-align: right; color: var(--ink); font-size: 19px; line-height: 30px;
  }

  .back__brand {
    position: absolute; left: 0; right: 0; top: 150px;
    display: flex; justify-content: center; align-items: center; gap: 14px;
  }
  .back__brand .brand__mark { background: var(--paper); width: 26px; height: 26px; }
  .back__brand .brand__name { color: var(--paper); font-size: 40px; }
  .tagline {
    position: absolute; left: 0; right: 0; top: 238px;
    text-align: center; color: var(--paper); font-size: 24px; letter-spacing: 3px;
  }
</style>
</head>
<body>
  <section class="card card--front">
    <div class="holder">
      <p class="holder__name">Daniel Marsh</p>
      <p class="holder__title">Managing Director</p>
    </div>
    <ul class="contact">
      <li class="contact__item">
        <svg class="contact__icon" viewBox="0 0 16 16"><path d="M2 5c0-2 2-3 6-3s6 1 6 3v2h-3V5.5H5V7H2z M4 8h8l2 6H2z"/></svg>
        044-987 650 321
      </li>
      <li class="contact__item">
        <svg class="contact__icon" viewBox="0 0 16 16"><path d="M4 1h8v14H4z M5.5 2.5v9h5v-9z M7 12.5h2v1.2H7z" fill-rule="evenodd"/></svg>
        044-987 650 321
      </li>
      <li class="contact__item">
        <svg class="contact__icon" viewBox="0 0 16 16"><path d="M1 3h14v10H1z M2 4l6 5 6-5" fill="none" stroke="#3a3a3a" stroke-width="1.6"/></svg>
        info@tessaron.com
      </li>
    </ul>
    <div class="divider"></div>
    <div class="brand">
      <span class="brand__mark"></span>
      <span class="brand__name">Tessaron LLC</span>
    </div>
    <p class="address">48 Harbour Lane, Suite 5<br>Northbridge, 204518</p>
  </section>

  <section class="card card--back">
    <div class="back__brand brand">
      <span class="brand__mark"></span>
      <span class="brand__name">Tessaron LLC</span>
    </div>
    <p class="tagline">clear past the noise</p>
  </section>
</body>
</html>
```